Exciting Personal Development Book Cover: TURN LUMA UP!

Design a Book Cover for my personal development book.
Title: Turn LUMA Up!
Author: Marcus Tillet
Tagline: A real-life solution to get unstuck and break free

My picture must make up the front cover as I need to build my brand and people should recognise me on book shelves. Bold and catchy. How you do it is up to you. There must be space for a short testimonial from a famous person who is currently reading my book. I uploaded a sample of what I made in Photoshop but I don't have design skills.

I've added a PDF of my book so you can read the chapter index and introduction to get a sense of the content.

Target Market(s)

Personal Development Self-Help Market

Industry/Entity Type

Personal Development

Font styles to use
Serif
Sans Serif

Requirements
Must have
• My picture as hero image on cover.
Nice to have
• Must have Title, Tagline and my author name. If possible LUMA stands for 'Ownership, Vision & Action' If there is a way to fit this somewhere great. If it's too much then it can go somewhere on the back.

```html
<!DOCTYPE html>
<html lang="en">
<head>
<meta charset="utf-8">
<title>Turn LUMA Up! – Book Cover Wrap</title>
<link rel="stylesheet" href="https://fonts.googleapis.com/css2?family=Anton&family=Quicksand:wght@300;400;700&family=Saira+Condensed:ital,wght@0,700;0,800;1,600;1,800&display=swap">
<style>
  :root {
    --page: #ffffff;
    --blue: #0a86f7;
    --ink: #0c0c0c;
    --white: #ffffff;
    --grey-dark: #3a3a3a;
    --grey-mid: #5c5c5c;
    --grey-light: #7a7a7a;
    --body-text: #e6e6e6;
  }
  * { margin: 0; padding: 0; box-sizing: border-box; }
  html, body {
    width: 848px; height: 1200px; overflow: hidden;
    background: var(--page);
  }
  .cover-wrap {
    position: absolute; left: 17px; top: 323px;
    width: 813px; height: 553px;
    background: radial-gradient(ellipse at 50% 45%, var(--grey-light) 0%, var(--grey-mid) 45%, var(--grey-dark) 100%);
    overflow: hidden;
  }
  .panel { position: absolute; top: 0; height: 553px; }
  .back-cover { left: 0; width: 369px;
    background: radial-gradient(ellipse at 50% 55%, #6e6e6e 0%, #565656 50%, #3b3b3b 100%); }
  .spine { left: 369px; width: 76px;
    background: linear-gradient(180deg, #454545, #5e5e5e 55%, #4a4a4a);
    box-shadow: inset 1px 0 0 rgba(0,0,0,.15), inset -1px 0 0 rgba(0,0,0,.15); }
  .front-cover { left: 445px; width: 368px;
    background: radial-gradient(ellipse at 55% 45%, #7c7c7c 0%, #5d5d5d 50%, #3c3c3c 100%); }

  .back-tagline {
    position: absolute; left: 14px; width: 341px; top: 52px;
    font-family: "Quicksand", sans-serif; font-weight: 300;
    font-size: 12.5px; line-height: 12px; color: var(--white); text-align: center;
  }
  .back-tagline strong { font-weight: 700; }
  .back-title { position: absolute; left: 0; top: 110px; }
  .blurb {
    position: absolute; left: 34px; width: 301px; top: 199px;
    font-family: "Quicksand", sans-serif; font-weight: 400;
    font-size: 10.6px; line-height: 17.1px; color: var(--body-text);
    text-align: justify; text-align-last: center;
  }
  .tagline-band {
    position: absolute; left: 0; bottom: 0; width: 813px; height: 35px;
    background: var(--blue);
  }
  .band-text {
    position: absolute; top: 0; height: 35px; line-height: 35px;
    font-family: "Saira Condensed", sans-serif; font-weight: 800;
    font-size: 13.5px; letter-spacing: .4px; color: var(--white);
    text-transform: uppercase; text-align: center; white-space: nowrap;
  }
  .band-back { left: 0; width: 369px; }
  .band-front { left: 445px; width: 368px; }
  .spine-title, .front-lockup { position: absolute; left: 0; top: 0; }
  .pillars {
    position: absolute; left: 30px; top: 474px;
    font-family: "Quicksand", sans-serif; font-weight: 400;
    font-size: 10px; line-height: 10.5px; color: var(--white);
  }
</style>
</head>
<body>
<main class="cover-wrap">
  <section class="panel back-cover">
    <p class="back-tagline">Stacking <strong>OWNERSHIP, VISION</strong> and <strong>ACTION</strong> to overcome pain<br>and the obstacles of life</p>
    <svg class="back-title" width="369" height="60" viewBox="0 0 369 60">
      <text x="61" y="48" textLength="244" lengthAdjust="spacingAndGlyphs"
            font-family="Anton, sans-serif" font-size="56" font-style="italic">
        <tspan fill="var(--ink)">TURN </tspan><tspan fill="var(--blue)">LUMA </tspan><tspan fill="var(--white)">UP!!</tspan>
      </text>
    </svg>
    <div class="blurb">
      <p>My picture must make up the front cover as I need to build my brand and people should recognise me on book shelves. Bold and catchy. How you do it is up to you. There must be space for a short testimonial from a famous person who is currently reading my book. I uploaded a sample of what I made in Photoshop but I don't have design skills.</p>
      <p>My picture must make up the front cover as I need to build my brand and people should recognise me on book shelves. Bold and catchy. How you do it is up to you. There must be space for a short testimonial from a famous person who is currently reading my book. I uploaded a sample of what I made in Photoshop but I don't have design skills.</p>
      <p>My picture must make up the front cover as I need to build my brand and people should recognise me on book shelves. Bold and catchy. How you do it is up to you. There must be space for a short testimonial from a famous person who is currently reading my book. I uploaded a sample of what I made in Photoshop but I don't have design skills.</p>
    </div>
  </section>

  <section class="panel spine">
    <svg class="spine-title" width="76" height="553" viewBox="0 0 76 553">
      <text transform="translate(10 98) rotate(90)" textLength="359" lengthAdjust="spacingAndGlyphs"
            font-family="Anton, sans-serif" font-size="80">
        <tspan fill="var(--ink)">TURN </tspan><tspan fill="var(--blue)">LUMA </tspan><tspan fill="var(--white)">UP!!</tspan>
      </text>
    </svg>
  </section>

  <section class="panel front-cover">
    <svg class="front-lockup" width="368" height="553" viewBox="0 0 368 553">
      <defs>
        <radialGradient id="portrait-tone" cx="50%" cy="40%" r="60%">
          <stop offset="0%" stop-color="#d9d9d9"/>
          <stop offset="55%" stop-color="#9a9a9a"/>
          <stop offset="100%" stop-color="#6a6a6a" stop-opacity="0"/>
        </radialGradient>
      </defs>
      <rect class="author-portrait" role="img" aria-label="Black and white portrait of the author smiling, arms crossed, in a white shirt"
            x="40" y="88" width="290" height="430" fill="url(#portrait-tone)"/>
      <text class="testimonial" x="196" y="38" text-anchor="middle" textLength="295" lengthAdjust="spacingAndGlyphs"
            font-family="'Saira Condensed', sans-serif" font-weight="600" font-style="italic" font-size="12" fill="var(--white)">‘OCCUS, QUIASS ITASPITI DOLUPTAS ALIT ET VOLO’ - NAME SURNAME</text>
      <text class="author-name" x="18" y="77" textLength="331" lengthAdjust="spacing"
            font-family="'Saira Condensed', sans-serif" font-weight="800" font-size="32" fill="var(--blue)">MARCUS TILLET</text>
      <text x="112" y="313" textLength="155" lengthAdjust="spacingAndGlyphs"
            font-family="Anton, sans-serif" font-style="italic" font-size="96" fill="var(--ink)">TURN</text>
      <text x="25" y="467" textLength="318" lengthAdjust="spacingAndGlyphs"
            font-family="Anton, sans-serif" font-size="208" fill="var(--blue)">LUMA</text>
      <text x="283" y="511" textLength="58" lengthAdjust="spacingAndGlyphs"
            font-family="Anton, sans-serif" font-size="48" fill="var(--white)">UP!!</text>
    </svg>
    <p class="pillars">OWNERSHIP<br>VISION<br>ACTION</p>
  </section>

  <div class="tagline-band">
    <p class="band-text band-back">A real-life solution to get unstuck and break free</p>
    <p class="band-text band-front">A real-life solution to get unstuck and break free</p>
  </div>
</main>
</body>
</html>
```